Oral Health Packaging Design

I need to redesign the products in our VELTRA Range of toothpastes and mouthwash.
1. VELTRA Toothpaste (http://www.mintvaleco.com.au/aus/serene-toothpaste.html)
2. VELTRA Tongue Gel (http://www.mintvaleco.com.au/aus/veltra-gel.html)
3. VELTRA (with TORVA P47) "airshield" (http://www.mintvaleco.com.au/aus/veltra-powder.html)
4. VELTRA (with TORVA R63 "gumshield" (New Product)
5. VELTRA Serene Rinse (two bottles mixed together) (http://www.mintvaleco.com.au/aus/serene-rinse.html)

I need all the products to look like a family.
TOOTHPASTE & MOUTHWASH
The toothpaste and tongue gel are used together. So we are dumping the airshield and serene names and rebranding under just VeltRa. Customer feedback is that they are embarrased to put these products in their bathroom in case someone sees them. So we are looking for a clean, corporate and clinical look that emphasises mouth health and maximising fresh breath.
The P47 and R63 can be used together but not necessary. These are our special blend of probiotics. By law we can only say that they treat bad breath, we are not allowed to talk about other health benefits. So I thought that images (maybe as a watermark behind the text might help). So looking to get a graphival look to these labels for the probiotics. Disctinction is that P47 is for fresh breath and R63 is to prevent tooth decay and Oral health
Serene Rinse comes in three strengths. It is two liquides mixed together. This rinse is used twice a week to knock down the bacteria to help the probitocis work

Initial stage is to get the family feel.
Next is the P47 and R63 labels
Next is the Toothpaste
Next is the Serene Rinse
Next is the tongue gel

Target Market(s)

People with bad breath or looking for maximum mouth health

Industry/Entity Type

Health

Requirements
Must have
• Corporate, clinical, neat and tidy should show confidence
Dropping the Airshield and Serene labels. Putting everything under VELTRA brand. However probiotics can have "airshield" at bottom of label for P47 and "gumshield" at bottom of label for R63
Nice to have
• I have uploaded two brochures of P47 and R63. I like the circle design around the P47 and the M18and I also like the colouring.
Should not have
• no medical claims

```html
<!DOCTYPE html>
<html lang="en">
<head>
<meta charset="utf-8">
<title>VELTRA Oral Care Range</title>
<link href="https://fonts.googleapis.com/css2?family=Montserrat:ital,wght@0,600;0,800;0,900;1,600&family=Open+Sans:wght@400;600;700&display=swap" rel="stylesheet">
<style>
  :root {
    --teal: #2bb7d2;
    --teal-dark: #1a93ad;
    --navy: #1f3a4b;
    --navy-deep: #17303f;
    --pink: #e2528c;
    --white: #ffffff;
    --cap: #f1f3f4;
    --amber: #6b3a14;
    --amber-dark: #3f200a;
    --gold: #d4a62a;
    --ink: #223;
  }
  * { box-sizing: border-box; margin: 0; padding: 0; }
  html, body { width: 1200px; height: 900px; overflow: hidden; background: var(--white); }
  body { position: relative; font-family: "Open Sans", Arial, sans-serif; color: var(--white); }

  /* ---------- tubes ---------- */
  .tube { position: absolute; top: 30px; width: 260px; height: 540px; }
  .tube-body {
    position: absolute; inset: 0 0 40px 0;
    clip-path: polygon(0 0, 100% 0, 90% 100%, 10% 100%);
    overflow: hidden;
  }
  .tube-crimp { position: absolute; top: 0; left: 0; right: 0; height: 14px; background: rgba(0,0,0,.12); }
  .tube-cap {
    position: absolute; bottom: 0; left: 22%; width: 56%; height: 48px;
    background: linear-gradient(90deg, #d9dcde, var(--cap) 40%, #ffffff 60%, #d4d7d9);
    border-radius: 0 0 6px 6px;
  }
  .tube--paste .tube-body { background: var(--teal); }
  .tube--gel .tube-body { background: var(--navy); }

  .check-pattern {
    position: absolute; top: 14px; left: 0; right: 0; height: 170px;
    background: linear-gradient(180deg, var(--navy) 0%, var(--teal-dark) 100%);
    opacity: .9;
  }
  .tube--gel .check-pattern { background: linear-gradient(180deg, var(--teal-dark), var(--navy)); }
  .pattern-corner { position: absolute; top: 14px; right: 0; width: 60%; height: 200px;
    background: linear-gradient(200deg, var(--teal-dark), var(--navy)); }

  .seal { position: absolute; top: 40px; right: 34px; width: 34px; height: 34px; border-radius: 50%;
    background: var(--gold); border: 3px solid #f4d67a; }

  .front-label { position: absolute; left: 26px; right: 26px; top: 196px; }
  .brand { font-family: "Montserrat", Arial, sans-serif; font-weight: 900; font-size: 40px; line-height: 1; letter-spacing: .5px; }
  .product { font-family: "Montserrat", Arial, sans-serif; font-weight: 800; font-size: 30px; line-height: 1.02; margin-top: 4px; }
  .tagline { font-family: "Montserrat", Arial, sans-serif; font-style: italic; font-weight: 600; font-size: 12px; margin-top: 4px; }
  .features { list-style: none; font-size: 10px; line-height: 1.55; margin-top: 22px; font-weight: 600; }
  .net { position: absolute; left: 34px; bottom: 34px; font-family: "Montserrat", Arial, sans-serif; font-weight: 800; font-size: 16px; }
  .net small { font-size: 8px; }

  .back-label { position: absolute; left: 40px; right: 34px; top: 200px; font-size: 9px; line-height: 1.5; }
  .back-label h3 { font-family: "Montserrat", Arial, sans-serif; font-weight: 800; font-size: 10px; text-align: center; margin-bottom: 8px; }
  .back-label--light { color: var(--ink); }
  .back-panel { position: absolute; top: 184px; left: 0; right: 0; bottom: 0; background: var(--white); }

  #paste-front { left: 50px; }
  #paste-back  { left: 320px; }
  #gel-front   { left: 620px; }
  #gel-back    { left: 890px; }

  /* ---------- rinse bottles ---------- */
  .bottle { position: absolute; top: 600px; width: 130px; height: 280px; }
  .bottle-cap { position: absolute; top: 0; left: 22%; width: 56%; height: 56px; background: var(--cap); border-radius: 8px 8px 2px 2px; }
  .bottle-shoulder { position: absolute; top: 52px; left: 0; right: 0; height: 40px; background: var(--cap); border-radius: 40px 40px 0 0; }
  .bottle-body { position: absolute; top: 88px; left: 0; right: 0; bottom: 0; background: var(--cap); border-radius: 0 0 10px 10px; overflow: hidden; }
  .bottle-label { position: absolute; top: 24px; left: 0; right: 0; height: 150px; background: var(--teal); padding: 26px 10px 0; }
  .mini-pattern { position: absolute; top: 0; left: 0; right: 0; height: 20px; background: linear-gradient(90deg, var(--navy), var(--teal-dark)); }
  .bottle-label .brand { font-size: 22px; }
  .bottle-label .product { display: inline-block; font-size: 17px; margin-top: 4px; padding: 2px 6px; }
  .bottle-label .note { font-size: 7px; line-height: 1.4; margin-top: 8px; }
  .bottle-label .vol { font-size: 8px; font-weight: 700; margin-top: 4px; }
  .product--pink { background: var(--pink); }
  #rinse-1 { left: 190px; }
  #rinse-2 { left: 330px; }

  /* ---------- probiotic jars ---------- */
  .jar { position: absolute; top: 640px; width: 130px; height: 240px; }
  .jar-lid { position: absolute; top: 0; left: 6%; width: 88%; height: 50px; background: var(--amber-dark); border-radius: 6px 6px 0 0; }
  .jar-body { position: absolute; top: 50px; left: 0; right: 0; bottom: 0; background: linear-gradient(90deg, var(--amber-dark), var(--amber) 45%, var(--amber-dark)); border-radius: 4px 4px 10px 10px; overflow: hidden; }
  .jar-label { position: absolute; top: 14px; left: 0; right: 0; height: 156px; background: var(--teal); padding: 24px 8px 0; }
  .jar-label .mini-pattern { height: 18px; }
  .jar-label .brand { font-size: 22px; }
  .jar-label .product { display: inline-block; font-size: 14px; padding: 2px 4px; margin-top: 3px; }
  .jar-label .strain { font-family: "Montserrat", Arial, sans-serif; font-weight: 800; font-size: 11px; margin-top: 4px; }
  .jar-label .note { font-size: 7px; margin-top: 3px; }
  .jar-label .count { font-size: 7px; font-weight: 700; margin-top: 5px; }
  .jar-label .line-name { position: absolute; left: 0; right: 0; bottom: 0; padding: 4px 8px; background: var(--navy); font-family: "Montserrat", Arial, sans-serif; font-weight: 800; font-size: 10px; letter-spacing: 1px; text-align: center; }
  .product--teal { background: var(--teal-dark); }
  #mouthwash-p47 { left: 560px; }
  #mouthwash-r63 { left: 710px; }
</style>
</head>
<body>

  <!-- Toothpaste, front -->
  <div class="tube tube--paste" id="paste-front">
    <div class="tube-body">
      <div class="check-pattern" role="img" aria-label="Navy and teal checkered pattern band"></div>
      <div class="tube-crimp"></div>
      <div class="seal"></div>
      <div class="front-label">
        <div class="brand">VELTRA</div>
        <div class="product">TOOTH<br>PASTE</div>
        <div class="tagline">Tooth &amp; Gum Cleaning.</div>
        <ul class="features">
          <li>Non</li>
          <li>Whitening Agents</li>
          <li>To Assure</li>
          <li>Your Teeth Last</li>
          <li>Whiter &amp; Cleaner</li>
        </ul>
      </div>
      <div class="net">100g <small>NET</small></div>
    </div>
    <div class="tube-cap"></div>
  </div>

  <!-- Toothpaste, back -->
  <div class="tube tube--paste" id="paste-back">
    <div class="tube-body">
      <div class="pattern-corner" role="img" aria-label="Navy and teal checkered pattern band"></div>
      <div class="tube-crimp"></div>
      <div class="back-panel"></div>
      <div class="back-label back-label--light">
        <h3>HOW TO USE VELTRA TOOTHPASTE</h3>
        <p>Squeeze a small amount onto a soft brush. Brush all tooth surfaces gently for two minutes, paying close attention to the gum line. Rinse well with water.</p>
        <p>Use twice daily, morning and night, for a clean and fresh mouth.</p>
        <p>Keep out of reach of children. Store below 30°C.</p>
      </div>
    </div>
    <div class="tube-cap"></div>
  </div>

  <!-- Tongue gel, front -->
  <div class="tube tube--gel" id="gel-front">
    <div class="tube-body">
      <div class="check-pattern" role="img" aria-label="Teal and navy checkered pattern band"></div>
      <div class="tube-crimp"></div>
      <div class="seal"></div>
      <div class="front-label">
        <div class="brand">VELTRA</div>
        <div class="product">TONGUE<br>GEL</div>
        <div class="tagline">Tongue Surface Cleaning.</div>
        <ul class="features">
          <li>Non-Abrasive Product</li>
          <li>Contains Fluoride &amp;</li>
          <li>Pyrophosphates</li>
          <li>So Can Also Be Used</li>
          <li>As A Toothpaste</li>
          <li>If Needed</li>
        </ul>
      </div>
      <div class="net">110g <small>NET</small></div>
    </div>
    <div class="tube-cap"></div>
  </div>

  <!-- Tongue gel, back -->
  <div class="tube tube--gel" id="gel-back">
    <div class="tube-body">
      <div class="pattern-corner" role="img" aria-label="Teal and navy checkered pattern band"></div>
      <div class="tube-crimp"></div>
      <div class="back-label">
        <h3>HOW TO USE VELTRA TONGUE GEL</h3>
        <p>Apply a small amount of gel to the back of the tongue. Gently scrape from back to front using a tongue cleaner. Rinse the cleaner after each stroke.</p>
        <p>Finish by brushing teeth with the remaining gel. Use daily for best results.</p>
      </div>
    </div>
    <div class="tube-cap"></div>
  </div>

  <!-- Rinse bottles -->
  <div class="bottle" id="rinse-1">
    <div class="bottle-cap"></div>
    <div class="bottle-shoulder"></div>
    <div class="bottle-body">
      <div class="bottle-label">
        <div class="mini-pattern" role="img" aria-label="Checkered pattern strip"></div>
        <div class="brand">VELTRA</div>
        <div class="product">ORAL<br>RINSE 1</div>
        <div class="note">Mix with Rinse 2 before use. Twice weekly.</div>
        <div class="vol">50ml</div>
      </div>
    </div>
  </div>

  <div class="bottle" id="rinse-2">
    <div class="bottle-cap"></div>
    <div class="bottle-shoulder"></div>
    <div class="bottle-body">
      <div class="bottle-label">
        <div class="mini-pattern" role="img" aria-label="Checkered pattern strip"></div>
        <div class="brand">VELTRA</div>
        <div class="product product--pink">ORAL<br>RINSE 2</div>
        <div class="note">Mix with Rinse 1 before use. Twice weekly.</div>
        <div class="vol">50ml</div>
      </div>
    </div>
  </div>

  <!-- Probiotic jars -->
  <div class="jar" id="mouthwash-p47">
    <div class="jar-lid"></div>
    <div class="jar-body">
      <div class="jar-label">
        <div class="mini-pattern" role="img" aria-label="Checkered pattern strip"></div>
        <div class="brand">VELTRA</div>
        <div class="product product--teal">MOUTHWASH</div>
        <div class="strain">TORVA P47</div>
        <div class="note">Probiotic lozenge for fresh breath</div>
        <div class="count">60 tablets</div>
        <div class="line-name">airshield</div>
      </div>
    </div>
  </div>

  <div class="jar" id="mouthwash-r63">
    <div class="jar-lid"></div>
    <div class="jar-body">
      <div class="jar-label">
        <div class="mini-pattern" role="img" aria-label="Checkered pattern strip"></div>
        <div class="brand">VELTRA</div>
        <div class="product product--pink">MOUTHWASH</div>
        <div class="strain">TORVA R63</div>
        <div class="note">Probiotic lozenge for oral health</div>
        <div class="count">60 tablets</div>
        <div class="line-name">gumshield</div>
      </div>
    </div>
  </div>

</body>
</html>
```